Book Cover design

The book title is Winter stayed longer in our little kitchen

I need a book cover design for a book about the unexpected loss of child. The book is a journal of my first 12 months after the loss of my son. An expression of how the grief never ends you just learn to cope. The journey to healing and hope.
Updates

Change in book title

Target Market(s)

Anyone that has experienced loss of love, career, physical loss, PTSD or experienced losing someone in an untimely manner

Font styles to use
Serif

Colors
0456a4
0792cd
33b8a4
acd136
ffffff
cee9f5
cfdeed

Requirements
Must have
• Beauty Depth

```html
<!DOCTYPE html>
<html lang="en">
<head>
<meta charset="utf-8">
<title>Winter stayed longer in our little kitchen — Full Cover Wrap</title>
<link rel="stylesheet" href="https://fonts.googleapis.com/css2?family=Playfair+Display:ital,wght@0,400;0,700;1,400&display=swap">
<style>
  :root {
    --page-bg: #f4f6f8;
    --deep-blue: #0456a4;
    --sky-blue: #0792cd;
    --teal: #33b8a4;
    --lime: #acd136;
    --white: #ffffff;
    --ice: #cee9f5;
    --mist: #cfdeed;
    --ink: #0b2f52;
  }
  html, body {
    margin: 0;
    width: 1200px;
    height: 1200px;
    overflow: hidden;
    background: var(--page-bg);
  }
  .cover-wrap {
    display: block;
    width: 1200px;
    height: 1200px;
  }
  .serif {
    font-family: "Playfair Display", Georgia, serif;
    fill: var(--white);
  }
  .title-front { font-size: 30px; font-weight: 700; }
  .title-back { font-size: 18px; font-weight: 700; }
  .author-label { font-size: 20px; font-weight: 400; }
  .author-name { font-size: 22px; font-weight: 700; }
  .back-author-label { font-size: 15px; font-weight: 400; }
  .back-author-name { font-size: 16px; font-weight: 700; }
  .tagline { font-size: 16px; font-style: italic; font-weight: 400; }
  .spine-author { font-size: 14px; font-style: italic; font-weight: 400; }
  .spine-title { font-size: 15px; font-weight: 700; }
</style>
</head>
<body>
<svg class="cover-wrap" viewBox="0 0 1200 1200" xmlns="http://www.w3.org/2000/svg">
  <defs>
    <radialGradient id="canopy-upper" cx="0.7" cy="0.3" r="0.9">
      <stop offset="0" stop-color="#ffffff"/>
      <stop offset="0.35" stop-color="#cfdeed"/>
      <stop offset="1" stop-color="#3f5f7e"/>
    </radialGradient>
    <radialGradient id="canopy-lower" cx="1" cy="0" r="1.15">
      <stop offset="0" stop-color="#cfdeed"/>
      <stop offset="0.5" stop-color="#6f8ea8"/>
      <stop offset="1" stop-color="#243d57"/>
    </radialGradient>
    <linearGradient id="wash-front" x1="0" y1="0" x2="1" y2="1">
      <stop offset="0" stop-color="#1d4f7c"/>
      <stop offset="0.4" stop-color="#0456a4"/>
      <stop offset="0.7" stop-color="#2f8fae"/>
      <stop offset="1" stop-color="#7fb8c9"/>
    </linearGradient>
    <linearGradient id="wash-back" x1="0" y1="0" x2="1" y2="1">
      <stop offset="0" stop-color="#2a6b9e"/>
      <stop offset="0.3" stop-color="#0456a4"/>
      <stop offset="0.55" stop-color="#2b9a96"/>
      <stop offset="0.8" stop-color="#1f5f8f"/>
      <stop offset="1" stop-color="#0a4a86"/>
    </linearGradient>
    <linearGradient id="tile-teal" x1="0" y1="0" x2="1" y2="1">
      <stop offset="0" stop-color="#229a88"/>
      <stop offset="0.5" stop-color="#5fd0bd"/>
      <stop offset="1" stop-color="#1f8f7f"/>
    </linearGradient>
    <linearGradient id="tile-blue" x1="0" y1="0" x2="1" y2="1">
      <stop offset="0" stop-color="#0572a8"/>
      <stop offset="0.5" stop-color="#3fb0e0"/>
      <stop offset="1" stop-color="#046a9c"/>
    </linearGradient>
    <linearGradient id="tile-mixed" x1="0" y1="0" x2="1" y2="1">
      <stop offset="0" stop-color="#acd136"/>
      <stop offset="0.45" stop-color="#33b8a4"/>
      <stop offset="0.75" stop-color="#cee9f5"/>
      <stop offset="1" stop-color="#0792cd"/>
    </linearGradient>
  </defs>

  <!-- Back cover -->
  <g class="back-cover">
    <rect class="back-wash" x="40" y="205" width="527" height="790" fill="url(#wash-back)"
          role="img" aria-label="Blue and teal watercolour texture"/>
    <line class="rule rule-top" x1="86" y1="246" x2="521" y2="246" stroke="var(--white)" stroke-width="3"/>
    <g class="back-title-tiles">
      <rect x="218" y="268" width="86" height="86" fill="var(--teal)" opacity="0.85"/>
      <rect x="304" y="268" width="86" height="86" fill="var(--deep-blue)" opacity="0.85"/>
      <rect x="218" y="354" width="86" height="86" fill="var(--ink)" opacity="0.9"/>
      <rect x="304" y="354" width="86" height="86" fill="var(--sky-blue)" opacity="0.85"/>
    </g>
    <text class="serif title-back" text-anchor="middle">
      <tspan x="304" y="320">Winter</tspan>
      <tspan x="304" y="344">stayed longer</tspan>
      <tspan x="304" y="368">in our little</tspan>
      <tspan x="304" y="392">kitchen</tspan>
    </text>
    <text class="serif tagline" x="290" y="584" text-anchor="middle" transform="rotate(-35 290 584)">The journey to healing and hope</text>
    <text class="serif back-author-label" x="304" y="896" text-anchor="middle">book by</text>
    <line class="rule rule-bottom" x1="86" y1="916" x2="521" y2="916" stroke="var(--white)" stroke-width="3"/>
    <text class="serif back-author-name" x="304" y="945" text-anchor="middle">Name Last Name</text>
  </g>

  <!-- Spine -->
  <g class="spine">
    <rect class="spine-band" x="567" y="205" width="66" height="790" fill="var(--deep-blue)"/>
    <text class="serif spine-author" x="600" y="240" transform="rotate(90 600 240)" dominant-baseline="middle">Name Last Name</text>
    <text class="serif spine-title" x="600" y="430" transform="rotate(90 600 430)" dominant-baseline="middle">Winter stayed longer in our little kitchen</text>
    <rect x="567" y="851" width="33" height="33" fill="var(--sky-blue)"/>
    <rect x="600" y="851" width="33" height="33" fill="var(--lime)"/>
    <rect x="567" y="884" width="33" height="33" fill="var(--teal)"/>
    <rect x="600" y="884" width="33" height="33" fill="var(--ice)"/>
  </g>

  <!-- Front cover -->
  <g class="front-cover">
    <rect class="forest-upper" x="856.5" y="205" width="263.5" height="395" fill="url(#canopy-upper)"
          role="img" aria-label="Photograph looking up through tall forest trees toward the sun"/>
    <rect class="forest-lower" x="633" y="600" width="223.5" height="395" fill="url(#canopy-lower)"
          role="img" aria-label="Photograph of tree trunks rising into the canopy"/>
    <rect class="front-wash" x="856.5" y="600" width="263.5" height="395" fill="url(#wash-front)"
          role="img" aria-label="Blue watercolour texture"/>
    <rect class="title-block" x="633" y="205" width="223.5" height="395" fill="var(--deep-blue)"/>

    <rect class="tile tile-lime" x="770.5" y="514" width="86" height="86" fill="var(--lime)"/>
    <rect class="tile tile-teal" x="856.5" y="514" width="86" height="86" fill="url(#tile-teal)"
          role="img" aria-label="Forest canopy tinted teal"/>
    <rect class="tile tile-blue" x="770.5" y="600" width="86" height="86" fill="url(#tile-blue)"
          role="img" aria-label="Forest canopy tinted blue"/>
    <rect class="tile tile-mixed" x="856.5" y="600" width="86" height="86" fill="url(#tile-mixed)"
          role="img" aria-label="Watercolour texture in lime, teal and ice blue"/>

    <text class="serif title-front" text-anchor="middle">
      <tspan x="744.75" y="300">Winter</tspan>
      <tspan x="744.75" y="342">stayed</tspan>
      <tspan x="744.75" y="384">longer</tspan>
      <tspan x="744.75" y="426">in our little</tspan>
      <tspan x="744.75" y="468">kitchen</tspan>
    </text>

    <text class="serif author-label" x="995" y="776" text-anchor="middle">book by</text>
    <text class="serif author-name" x="995" y="826" text-anchor="middle">Name Last Name</text>
  </g>
</svg>
</body>
</html>
```